Retail Label Design - Hand Sanitizer

LUMORA is Holvane Canadas legacy brand. For decades Holvane Canada has been trusted by our customers to provide unmatched capability in the revitalization of surfaces and materials. We are proud to relaunch LUMORATM with the same promise, but oriented towards a new challenge: meeting the demand for solutions to aid in our collective fight against COVID-19.

LUMORATM Ethanol Hand Sanitizer is the first official relaunch product – and 80% alcohol based sanitizer, free from fragrance and dye.

We want to maintain a cool and clean feel for the labels – reflective of the product. Ideally if we could incorporate a retro feel to the packaging, we would be very happy.

This label will need to be done to 3 different specs to suit a 235ml, 500ml and 4L package. We would like to start with the 500ml label. I have attached the dieline, (047-KAB) for the 500ml Package. I have also attached product info, logo and brand info.

The only requirements on the front panel is the logo, product name (Ethanol Gel Hand Sanitizer) and the quantity(473ml), space for barcode on back + info provided. the rest we will leave up to your expertise.

Font styles to use
Serif
Sans Serif

Requirements
Must have
• Logo
Product name
Quantity
Information on back panel provided.

```html
<!DOCTYPE html>
<html lang="en">
<head>
<meta charset="utf-8">
<title>LUMORA Ethanol Gel Hand Sanitizer – 473ml Label</title>
<link rel="stylesheet" href="https://fonts.googleapis.com/css2?family=Montserrat:wght@300;400;500;600;700;800&display=swap">
<style>
  :root{
    --bg:#d5d5d5;
    --navy:#073b57;
    --orange:#ef8148;
    --teal:#97d6d2;
    --white:#ffffff;
    --warn-warm:#fce7dd;
    --warn-cool:#dbe4e7;
    --ink:#1f3f52;
  }
  *{box-sizing:border-box;margin:0;padding:0}
  html,body{width:960px;height:1200px;overflow:hidden;background:var(--bg)}
  body{position:relative;font-family:"Montserrat",sans-serif;color:var(--navy)}

  .label{position:absolute;left:87px;width:788px;height:530px;background:var(--white);
    box-shadow:6px 6px 8px rgba(0,0,0,.28);overflow:hidden}
  .label--a{top:43px}
  .label--b{top:622px}
  .label__shapes{position:absolute;inset:0;width:788px;height:530px}

  .spine{position:absolute;left:0;top:0;width:29px;height:530px;background:var(--orange)}
  .spine__text{position:absolute;left:7px;bottom:13px;writing-mode:vertical-rl;transform:rotate(180deg);
    color:var(--white);font-size:8.6px;font-weight:400;white-space:nowrap;line-height:1}
  .spine__text b{font-weight:700}

  .brand-name{position:absolute;font-weight:800;color:var(--navy);letter-spacing:1px;line-height:1}
  .brand-name--small{left:128px;top:30px;font-size:28px}
  .brand-name--large{left:478px;top:76px;font-size:52px}

  .back-title{position:absolute;font-size:13.4px;font-weight:400;color:var(--navy);white-space:nowrap}
  .back-title b{font-weight:700}
  .label--a .back-title{left:92px;top:77px}
  .label--b .back-title{left:101px;top:75px}

  .facts{position:absolute;left:43px;font-size:5.75px;line-height:8.1px;color:var(--ink);text-align:justify}
  .facts p{margin-bottom:2.4px}
  .facts p.tight{margin-bottom:0}
  .facts b{font-weight:700;color:var(--navy)}
  .label--a .facts{top:100px;width:301px}
  .label--b .facts{top:96px;width:318px}

  .warning{position:absolute;left:45px;top:364px;width:296px;font-size:5.75px;line-height:8.2px;color:var(--ink);text-align:justify}
  .warning b{font-weight:700;color:var(--navy)}

  .on-orange{position:absolute;left:43px;top:370px;width:320px;font-size:5.75px;line-height:8.2px;color:var(--white)}
  .on-navy{position:absolute;left:43px;top:405px;width:318px;font-size:5.75px;line-height:8.2px;color:var(--white);text-align:justify}
  .on-orange b,.on-navy b{font-weight:700}

  .barcode-space{position:absolute;top:453px;width:125px;height:62px;background:var(--white)}
  .label--a .barcode-space{left:42px}
  .label--b .barcode-space{left:45px}

  .maker{position:absolute;left:240px;top:461px;font-size:5.6px;color:var(--white)}
  .label--b .maker{left:239px;top:455px}
  .icons{position:absolute;left:177px;top:499px;width:60px;height:18px}

  .front-head{position:absolute;left:456px;font-size:26.5px;font-weight:700;color:var(--navy);white-space:nowrap;line-height:1}
  .front-head span{font-weight:400}
  .front-head--en{top:203px}
  .front-head--fr1{top:240px}
  .front-head--fr2{top:270px}
  .claim{position:absolute;left:500px;top:308px;width:180px;text-align:center;font-size:19.5px;font-weight:300;color:var(--navy);white-space:nowrap}

  .strength{position:absolute;left:484px;top:364px;font-size:37px;font-weight:700;color:var(--white);line-height:1;letter-spacing:-.5px}
  .strength-label{position:absolute;left:576px;top:365px;font-size:14.5px;font-weight:400;color:var(--white);line-height:16.5px;white-space:nowrap}

  .free{position:absolute;right:128px;top:485px;font-size:18.5px;font-weight:300;color:var(--white);white-space:nowrap}
  .volume{position:absolute;left:682px;top:478px;font-size:27px;font-weight:500;color:var(--navy);line-height:1}
</style>
</head>
<body>

<section class="label label--a">
  <svg class="label__shapes" viewBox="0 0 788 530" aria-hidden="true">
    <polygon points="29,0 155,0 29,405" fill="var(--teal)"/>
    <polygon points="788,135 788,530 662,530" fill="var(--teal)"/>
    <polygon points="368,363 715,363 703,400 360,400" fill="var(--orange)"/>
    <polygon points="29,400 703,400 662,530 29,530" fill="var(--navy)"/>
    <polygon points="29,363 369,363 360,400 29,400" fill="var(--warn-warm)"/>
    <polygon points="29,400 360,400 345,448 29,448" fill="var(--warn-cool)"/>
  </svg>

  <div class="spine"><p class="spine__text"><b>LUMORA</b>&nbsp;&nbsp;&nbsp;<b>Ethanol</b> gel <b>Hand Sanitizer</b> meets <b>Health Canada</b> and the <b>World Health Organization Standards</b></p></div>

  <p class="brand-name brand-name--small">LUMORA</p>
  <h2 class="back-title">Ethanol Gel <b>HAND SANITIZER</b></h2>

  <div class="facts">
    <p class="tight"><b>Drug facts/Info-médicament</b><br>
    <b>Active ingredient/Ingrédients actif:</b> Ethyl alcohol (70%), Alcool éthylique (70 %).<br>
    <b>Inactive ingredients/Ingrédients inactifs:</b> Glycerin, hydroxypropyl methylcellulose stearoxy ether, sodium chloride, acid blue 25, peppermint essential oil, distilled water, citral, dipropylene glycol, linalool, citronellol, coumarin. Glycérine, hydroxypropyl methylcellulose stearoxy ether, chlorure de sodium, bleu acide 25, huile essentielle de menthe poivrée, eau distillée, citral, dipropylene glycol, linalool, citronello, coumarin.</p>
    <p style="margin-top:2.4px"><b>Purpose/Fin:</b> Antibacterial, antiseptic (skin) cleanser. Nettoyant antibactérien et antiseptique (pour la peau).</p>
    <p><b>Use/Usages:</b> Kills harmful bacteria/germs. Helps prevent spread of bacteria. Tue les bactéries/germes nocifs. Contribue à prévenir la propagation des bactéries.</p>
    <p><b>Dose/Dose:</b><br>
    <b>Children 2 - 11 years/Enfants de 2 à 11 ans</b> — Rub thoroughly into hands for at least 30 seconds. Allow to dry. Supervise children when they use this product. For occasional and personal domestic use.<br>
    <b>Adolescents 12 - 17 years/Adolescents de 12 à 17 ans</b> — Rub thoroughly into hands for at least 30 seconds. Allow to dry. Supervise children when they use this product. For occasional and personal domestic use. Bien frotter pendant au moins 30 secondes. Laisser sécher. Superviser les enfants durant l'utilisation de ce produit. Pour une utilisation occasionnelle pour usage domestique personnel.<br>
    <b>Adults 18 years &amp; older/Adultes 18 ans et plus</b> — Rub thoroughly into hands for at least 30 seconds. Allow to dry. Supervise children when they use this product. For occasional and personal domestic use. Bien frotter pendant au moins 30 secondes. Laisser sécher. Superviser les enfants durant l'utilisation de ce produit. Pour une utilisation occasionnelle pour usage domestique personnel.</p>
    <p><b>Contraindications/Contre-indication(s):</b> Do not use on children/infants less than 2 years of age (unless directed by a doctor/ physician/ health care practitioner/ health care provider/ health care professional). Ne pas utiliser sur les enfants/nourrissons de moins de 2 ans (sauf sur l'avis d'un médecin/ docteur/ praticien de soins de santé/ fournisseur de soins de santé/ professionnel de la santé).</p>
    <p><b>Directions/Mode d'emploi:</b> Put a thumbnail-sized amount on your palm and rub hands together until dry. Mettre une petite quantité de produit dans la paume et se frotter les mains jusqu'à ce qu'elles soient sèches.</p>
  </div>

  <div class="warning">
    <b>Warning/Avertissement:</b><br>
    <b>Flammable</b> — keep away from open flame and sources of heat. For external use only. Keep out of reach of children. If swallowed, call a poison control centre or get medical help right away. Stop use and consult health care professional if irritation develops. When using this product avoid contact with eyes. If contact occurs, rinse thoroughly with water.<br>
    <b>Inflammable</b> — tenir à l'écart des flammes nues et des sources de chaleur. Pour usage externe seulement. Tenir hors de la portée des enfants. En cas d'ingestion, appeler immédiatement un centre antipoison ou demander immédiatement de l'aide médicale. En cas d'irritation, cesser toute utilisation et consulter un professionnel de la santé. Éviter tout contact avec les yeux lors de l'utilisation. Si le produit entre en contact avec les yeux, rincer soigneusement avec de l'eau.
  </div>

  <div class="barcode-space" aria-label="Barcode area"></div>
  <p class="maker">Manufactured and Distributed by:</p>
  <svg class="icons" viewBox="0 0 60 18" aria-label="Recycling, disposal and 12 month shelf-life icons" role="img">
    <g fill="none" stroke="var(--white)" stroke-width="1.6">
      <polygon points="7,2 13,12 1,12"/>
      <path d="M24 7 h6 l-1 9 h-4 z"/>
      <circle cx="23" cy="3.5" r="1.6" fill="var(--white)" stroke="none"/>
      <rect x="41" y="5" width="15" height="11" rx="1.5"/>
      <path d="M41 5 q7.5 -4 15 0"/>
    </g>
    <text x="48.5" y="14" font-size="5" font-family="Montserrat, sans-serif" font-weight="700" fill="var(--white)" text-anchor="middle">12M</text>
  </svg>

  <p class="brand-name brand-name--large">LUMORA</p>
  <h1 class="front-head front-head--en">HAND SANITIZER <span>Gel</span></h1>
  <p class="front-head front-head--fr1">ANTISEPTIQUE</p>
  <p class="front-head front-head--fr2">POUR LES MAINS <span>Gel</span></p>
  <p class="claim">kills 99.9% of germs</p>
  <p class="strength">70%</p>
  <p class="strength-label">Ethyl Alcohol<br>d'alcool éthylique</p>
  <p class="free">perfume and dye free</p>
  <p class="volume">473ml</p>
</section>

<section class="label label--b">
  <svg class="label__shapes" viewBox="0 0 788 530" aria-hidden="true">
    <polygon points="29,0 154,0 29,400" fill="var(--teal)"/>
    <polygon points="788,135 788,530 662,530" fill="var(--teal)"/>
    <polygon points="33,365 715,365 704,400 29,400" fill="var(--orange)"/>
    <polygon points="29,400 704,400 662,530 29,530" fill="var(--navy)"/>
  </svg>

  <div class="spine"><p class="spine__text"><b>LUMORA</b>&nbsp;&nbsp;&nbsp;<b>Ethanol</b> gel <b>Hand Sanitizer</b> meets <b>Health Canada</b> and the <b>World Health Organization Standards</b></p></div>

  <p class="brand-name brand-name--small" style="left:132px;top:28px">LUMORA</p>
  <h2 class="back-title">Ethanol Gel <b>HAND SANITIZER</b></h2>

  <div class="facts">
    <p class="tight"><b>Drug facts/Info-médicament</b><br>
    <b>Active ingredient/Ingrédients actif:</b> Ethyl alcohol (70%), Alcool éthylique (70 %).<br>
    <b>Inactive ingredients/Ingrédients inactifs:</b> Glycerin, hydroxypropyl methylcellulose stearoxy ether, sodium chloride, acid blue 25, peppermint essential oil, distilled water, citral, dipropylene glycol, linalool, citronellol, coumarin. Glycérine, hydroxypropyl methylcellulose stearoxy ether, chlorure de sodium, bleu acide 25, huile essentielle de menthe poivrée, eau distillée, citral, dipropylene glycol, linalool, citronello, coumarin.</p>
    <p style="margin-top:3.5px"><b>Purpose/Fin:</b> Antibacterial, antiseptic (skin) cleanser. Nettoyant antibactérien et antiseptique (pour la peau).</p>
    <p style="margin-top:3.5px"><b>Use/Usages:</b> Kills harmful bacteria/germs. Helps prevent spread of bacteria. Tue les bactéries/germes nocifs. Contribue à prévenir la propagation des bactéries.</p>
    <p><b>Dose/Dose:</b><br>
    <b>Children 2 - 11 years/Enfants de 2 à 11 ans</b> — Rub thoroughly into hands for at least 30 seconds. Allow to dry. Supervise children when they use this product. For occasional and personal domestic use.<br>
    <b>Adolescents 12 - 17 years/Adolescents de 12 à 17 ans</b> — Rub thoroughly into hands for at least 30 seconds. Allow to dry. Supervise children when they use this product. For occasional and personal domestic use. Bien frotter pendant au moins 30 secondes. Laisser sécher. Superviser les enfants durant l'utilisation de ce produit. Pour une utilisation occasionnelle pour usage domestique personnel.<br>
    <b>Adults 18 years &amp; older/Adultes 18 ans et plus</b> — Rub thoroughly into hands for at least 30 seconds. Allow to dry. Supervise children when they use this product. For occasional and personal domestic use. Bien frotter pendant au moins 30 secondes. Laisser sécher. Superviser les enfants durant l'utilisation de ce produit. Pour une utilisation occasionnelle pour usage domestique personnel.</p>
    <p><b>Warning/Avertissement:</b><br>
    <b>Flammable</b> — keep away from open flame and sources of heat. For external use only. Keep out of reach of children. If swallowed, call a poison control centre or get medical help right away. Stop use and consult health care professional if irritation develops. When using this product avoid contact with eyes. If contact occurs, rinse thoroughly with water.<br>
    <b>Inflammable</b> — tenir à l'écart des flammes nues et des sources de chaleur. Pour usage externe seulement. Tenir hors de la portée des enfants. En cas d'ingestion, appeler immédiatement un centre antipoison ou demander immédiatement de l'aide médicale. En cas d'irritation, cesser toute utilisation et consulter un professionnel de la santé. Éviter tout contact avec les yeux lors de l'utilisation. Si le produit entre en contact avec les yeux, rincer soigneusement avec de l'eau.</p>
  </div>

  <p class="on-orange"><b>Directions/Mode d'emploi:</b> Put a thumbnail-sized amount on your palm and rub hands together until dry. Mettre une petite quantité de produit dans la paume et se frotter les mains jusqu'à ce qu'elles soient sèches.</p>
  <p class="on-navy"><b>Contraindications/Contre-indication(s):</b> Do not use on children/infants less than 2 years of age (unless directed by a doctor/ physician/ health care practitioner/ health care provider/ health care professional). Ne pas utiliser sur les enfants/nourrissons de moins de 2 ans (sauf sur l'avis d'un médecin/ docteur/ praticien de soins de santé/ fournisseur de soins de santé/ professionnel de la santé).</p>

  <div class="barcode-space" aria-label="Barcode area"></div>
  <p class="maker">Manufactured and Distributed by:</p>
  <svg class="icons" viewBox="0 0 60 18" aria-label="Recycling, disposal and 12 month shelf-life icons" role="img">
    <g fill="none" stroke="var(--white)" stroke-width="1.6">
      <polygon points="7,2 13,12 1,12"/>
      <path d="M24 7 h6 l-1 9 h-4 z"/>
      <circle cx="23" cy="3.5" r="1.6" fill="var(--white)" stroke="none"/>
      <rect x="41" y="5" width="15" height="11" rx="1.5"/>
      <path d="M41 5 q7.5 -4 15 0"/>
    </g>
    <text x="48.5" y="14" font-size="5" font-family="Montserrat, sans-serif" font-weight="700" fill="var(--white)" text-anchor="middle">12M</text>
  </svg>

  <p class="brand-name brand-name--large">LUMORA</p>
  <h1 class="front-head front-head--en">HAND SANITIZER <span>Gel</span></h1>
  <p class="front-head front-head--fr1">ANTISEPTIQUE</p>
  <p class="front-head front-head--fr2">POUR LES MAINS <span>Gel</span></p>
  <p class="claim">kills 99.9% of germs</p>
  <p class="strength" style="top:366px">70%</p>
  <p class="strength-label" style="top:367px">Ethyl Alcohol<br>d'alcool éthylique</p>
  <p class="free">perfume and dye free</p>
  <p class="volume">473ml</p>
</section>

</body>
</html>
```